Letterhead Design Project

Based on the attached logo we would like have a designed of stationary.
As we are a management consulting company focused on business development dealing with C-level and one level below we new business cards.
We have decided to use KRM (Northvale Advisory Partners) as the business name. The legal name will be Northvale Advisory Partners ApS but we will brand us under KRM. The tack line is “Shaping Lasting Gains” if we need one.
For legal reasons we need to have the legal name on the letters together with the company no. (cvr. nr. 58190476)
We want to signal the following:
- Serious
- Professional
- Creating Result
- Capable of thinking out of the box and creative
- Fast reactions we will be there when needed
What we do not want to be view as is:
- To smart
- We know better
- We can fix it yesterday
Our Value Proposition is two sited:
- Increasing revenue
- Reduced sales cost or increased efficiency
Therefore, companies can call us when they want to grow or they need to be more efficient.
Our business cards should have a two sided print with the logo incl. the tack line on one side and the detailed information on the other site.
We need to have the following information on the letter head:
- Legal company name
- Cvr nr.
- Address incl. country name (Denmark)
- Main number
- Wed address
Symbols are welcome to be used to guide for the above information.
The following information are expected to be in the personal signature of the letter.
- Name
- Title
- Mobile number
- E-mail address
Updates
Some of you has requested our specific details so here they come:
- Address incl. country name (Denmark): Lyngholmvej 42, 3460 Birkerød, Denmark
- Main number: +45 7381 5502
- Wed address: www.krmgrowth.com
Mobile no. are +45 xxxx xxxx or +45 2857 3016
Our e-mail looks like this: firstname.seconname@KRMGROWTH.COM or for me: henrik.dalgaard@krmgrowth.com
We need the design (file) as finish as posible so we just need to add personal details before printing.
Please be aware that we will prefer designs where we can print the full letter incl. design. As we are communicating on e-mails with pdf versions of the letter we also need to have a design which will print on the clients printers.
Target Market(s)
C level and one level below.
Major local and international Companies.
Industry/Entity Type
Management Consulting
Font styles to use
Colors
Designer to choose colors to be used in the design.
Requirements
Must have
- Use of our logo without tack line

```html
<!DOCTYPE html>
<html lang="en">
<head>
<meta charset="utf-8">
<title>KRM Letterhead</title>
<link rel="stylesheet" href="https://fonts.googleapis.com/css2?family=Questrial&display=swap">
<style>
  :root {
    --backdrop: #e8e8e8;
    --paper: #ffffff;
    --brand-blue: #1f64ad;
    --band-grey: #5f6670;
    --text-grey: #555b63;
  }
  * { margin: 0; padding: 0; box-sizing: border-box; }
  html, body {
    width: 1200px;
    height: 936px;
    overflow: hidden;
    background: var(--backdrop);
    font-family: "Questrial", "Century Gothic", sans-serif;
  }
  .letterhead {
    position: absolute;
    left: 296px;
    top: 38px;
    width: 608px;
    height: 860px;
    background: var(--paper);
    box-shadow: 0 2px 10px rgba(0,0,0,0.12);
  }
  .brand-name {
    position: absolute;
    left: 58px;
    top: 70px;
    font-size: 46px;
    line-height: 1;
    color: var(--brand-blue);
    letter-spacing: 1px;
  }
  .footer-band {
    position: absolute;
    left: 0;
    right: 0;
    bottom: 0;
    height: 11px;
    display: flex;
    gap: 4px;
  }
  .footer-band .band-grey { flex: 0 0 45%; background: var(--band-grey); }
  .footer-band .band-blue { flex: 1; background: var(--brand-blue); }
  .legal-info, .contact-info {
    position: absolute;
    bottom: 24px;
    font-size: 9px;
    line-height: 13px;
    color: var(--text-grey);
  }
  .legal-info { left: 58px; }
  .contact-info {
    left: calc(45% + 4px);
    display: flex;
    gap: 16px;
  }
  .contact-address { font-style: normal; }
  .contact-item {
    display: flex;
    align-items: center;
    gap: 5px;
    white-space: nowrap;
  }
  .contact-item svg { width: 9px; height: 9px; flex: none; }
</style>
</head>
<body>
  <main class="letterhead">
    <div class="brand-name">KRM</div>

    <div class="legal-info">
      <p>Northvale Advisory Partners ApS</p>
      <p>Company Nr.: 58190476</p>
    </div>

    <div class="contact-info">
      <address class="contact-address">
        <p>Lyngholmvej 42, 4180</p>
        <p>Sorø, Denmark</p>
      </address>
      <div class="contact-phones">
        <p class="contact-item">
          <svg viewBox="0 0 10 10" aria-hidden="true"><circle cx="5" cy="5" r="5" fill="var(--brand-blue)"/><path d="M3.2 2.6l1 .9-.5.7c.3.6.7 1 1.3 1.3l.7-.5.9 1-.6.7C4.6 6.5 3.5 5.4 3 3.3z" fill="#fff"/></svg>
          +45 2857 3016
        </p>
        <p class="contact-item">
          <svg viewBox="0 0 10 10" aria-hidden="true"><circle cx="5" cy="5" r="5" fill="var(--brand-blue)"/><rect x="2.8" y="3.6" width="4.4" height="3" fill="#fff"/><rect x="3.6" y="2.6" width="2.8" height="1.2" fill="#fff"/></svg>
          +45 2857 3019
        </p>
      </div>
      <div class="contact-web">
        <p class="contact-item">
          <svg viewBox="0 0 10 10" aria-hidden="true"><circle cx="5" cy="5" r="5" fill="var(--brand-blue)"/><rect x="2.6" y="3.2" width="4.8" height="3.4" fill="#fff"/><path d="M2.6 3.2L5 5.2l2.4-2" stroke="var(--brand-blue)" stroke-width=".6" fill="none"/></svg>
          info@krmgrowth.com
        </p>
        <p class="contact-item">
          <svg viewBox="0 0 10 10" aria-hidden="true"><circle cx="5" cy="5" r="5" fill="var(--brand-blue)"/><circle cx="5" cy="5" r="2.6" fill="none" stroke="#fff" stroke-width=".7"/><path d="M2.4 5h5.2M5 2.4v5.2" stroke="#fff" stroke-width=".6"/></svg>
          www.krmgrowth.com
        </p>
      </div>
    </div>

    <div class="footer-band">
      <div class="band-grey"></div>
      <div class="band-blue"></div>
    </div>
  </main>
</body>
</html>
```